Business card design for Bront Engineering Qavo

We need a new business card design along with all the necessary to place an order. The company is Bront Engineering Qavo and we recently updated our logo.

```html
<!DOCTYPE html>
<html lang="en">
<head>
<meta charset="utf-8">
<title>Bront Engineering Qavo – Business Card</title>
<link href="https://fonts.googleapis.com/css2?family=Montserrat:wght@400;500;600;700&display=swap" rel="stylesheet">
<style>
  :root {
    --stage: #e9e6e1;
    --card-light: #ffffff;
    --card-dark: #000000;
    --gold: #e2b828;
    --steel: #8f8f8f;
    --ink: #1c1c1c;
  }
  * { margin: 0; padding: 0; box-sizing: border-box; }
  html, body { width: 900px; height: 1200px; overflow: hidden; }
  body {
    background: var(--stage);
    font-family: "Montserrat", sans-serif;
    position: relative;
  }
  .card {
    position: absolute;
    border-radius: 22px;
    overflow: hidden;
  }
  .card--front { left: 80px; top: 130px; width: 742px; height: 442px; background: var(--card-light); }
  .card--back { left: 78px; top: 638px; width: 744px; height: 440px; background: var(--card-dark); }

  .brand {
    position: absolute;
    display: flex;
    align-items: center;
    gap: 14px;
    color: var(--steel);
    font-weight: 600;
    letter-spacing: 1px;
    text-transform: uppercase;
    white-space: nowrap;
  }
  .brand__mark { background: var(--gold); flex: none; }
  .brand__name { display: block; }

  .card--front .brand { left: 40px; top: 50px; font-size: 25px; line-height: 31px; }
  .card--front .brand__mark { width: 40px; height: 40px; }
  .card--front .brand__line { display: block; }

  .card--back .brand { left: 0; right: 0; top: 192px; justify-content: center; font-size: 37px; }
  .card--back .brand__mark { width: 42px; height: 42px; }

  .feature-block {
    position: absolute;
    left: 380px; top: 100px;
    width: 326px; height: 300px;
    background: linear-gradient(160deg, #f1d466 0%, var(--gold) 45%, #b8b8b8 100%);
    opacity: 0.9;
  }

  .holder { position: absolute; left: 38px; top: 186px; }
  .holder__name { color: var(--gold); font-weight: 600; font-size: 25px; line-height: 1.1; }
  .holder__role { color: var(--ink); font-size: 16px; margin-top: 6px; font-weight: 400; }

  .address { position: absolute; left: 38px; top: 262px; color: var(--ink); font-size: 16px; line-height: 20px; }

  .contacts { position: absolute; left: 38px; top: 320px; list-style: none; }
  .contacts li {
    display: flex; align-items: center; gap: 9px;
    color: var(--ink); font-size: 16px; height: 28px;
  }
  .contacts svg { width: 16px; height: 16px; fill: var(--gold); flex: none; }
</style>
</head>
<body>
  <section class="card card--front">
    <div class="brand">
      <span class="brand__mark"></span>
      <span class="brand__name">
        <span class="brand__line">Bront</span>
        <span class="brand__line">Engineering Qavo</span>
      </span>
    </div>
    <div class="feature-block" role="img" aria-label="Large company emblem in gold and grey"></div>

    <div class="holder">
      <h1 class="holder__name">Dale Morencio</h1>
      <p class="holder__role">Managing Director</p>
    </div>

    <p class="address">42 Summit Crossing Plaza<br>Fairbrook, NJ 07311 USA</p>

    <ul class="contacts">
      <li>
        <svg viewBox="0 0 24 24"><path d="M6.6 10.8a15 15 0 0 0 6.6 6.6l2.2-2.2a1 1 0 0 1 1-.25 11.4 11.4 0 0 0 3.6.57 1 1 0 0 1 1 1V20a1 1 0 0 1-1 1A17 17 0 0 1 3 4a1 1 0 0 1 1-1h3.5a1 1 0 0 1 1 1c0 1.25.2 2.45.57 3.6a1 1 0 0 1-.25 1z"/></svg>
        (555)410-2736
      </li>
      <li>
        <svg viewBox="0 0 24 24"><path d="M2 5h20v2l-10 6L2 7zM2 9.3l10 6 10-6V19H2z"/></svg>
        inffo@yourwebsitename.com
      </li>
      <li>
        <svg viewBox="0 0 24 24"><path d="M12 2a10 10 0 1 0 0 20 10 10 0 0 0 0-20zm-1 17.9A8 8 0 0 1 4.1 11H7c.1 2.5.9 5 2.2 7zM4.1 9A8 8 0 0 1 11 4.1V9zm9 10.9V13h6.9a8 8 0 0 1-6.9 6.9zM13 11V4.1A8 8 0 0 1 19.9 11z"/></svg>
        www.yourwebsitename.com
      </li>
    </ul>
  </section>

  <section class="card card--back">
    <div class="brand"><span class="brand__mark"></span>Bront Engineering Qavo</div>
  </section>
</body>
</html>
```